Please create a custom business card for 'Adventures beyond any map'. The logo is attached to this brief.

Here is the link to the logo project : http://work.plumvessel.example/task.aspx?id=319207

Questions can be posted on the Discussion Board.

```html
<!DOCTYPE html>
<html lang="en">
<head>
<meta charset="utf-8">
<title>Nomadia — Business Card</title>
<link rel="stylesheet" href="https://fonts.googleapis.com/css2?family=Open+Sans:wght@400;600;700&display=swap">
<style>
  :root {
    --stage: #d9d9d9;
    --card-dark: #3a3a3c;
    --card-light: #ffffff;
    --brand-red: #ec1c0c;
    --text-dark: #3a3a3a;
    --text-light: #f2f2f2;
  }
  * { box-sizing: border-box; margin: 0; padding: 0; }
  html, body {
    width: 1200px; height: 900px; overflow: hidden;
    background: var(--stage);
    font-family: "Open Sans", Arial, sans-serif;
  }
  .stage { position: relative; width: 1200px; height: 900px; }

  .card {
    position: absolute; width: 560px; height: 320px;
    border-radius: 4px; overflow: hidden;
    box-shadow: 0 10px 26px rgba(0,0,0,.25);
  }

  /* Back of card */
  .card--back {
    left: 560px; top: 80px;
    background: var(--card-dark);
    display: flex; flex-direction: column; align-items: center; justify-content: center;
  }
  .brand { display: flex; align-items: center; gap: 14px; }
  .brand__dot { width: 34px; height: 34px; background: var(--brand-red); }
  .brand__name {
    font-weight: 700; font-size: 52px; line-height: 1;
    color: var(--brand-red); letter-spacing: 1px;
  }
  .card--back .web {
    margin-top: 12px; color: var(--text-light);
    font-size: 15px; letter-spacing: 6px;
  }

  /* Front of card */
  .card--front {
    left: 120px; top: 470px;
    background: var(--card-light);
  }
  .front__panel { position: absolute; inset: 0; }
  .front__content { position: absolute; left: 40px; top: 28px; }
  .front__brand {
    font-weight: 700; font-size: 56px; line-height: 1;
    color: var(--brand-red); letter-spacing: 1px;
  }
  .person { margin-top: 14px; }
  .person__name { font-weight: 700; font-size: 20px; color: var(--brand-red); }
  .person__role { font-size: 15px; color: var(--text-dark); }
  .address { margin-top: 10px; font-size: 14px; line-height: 1.35; color: var(--text-dark); }
  .contacts { margin-top: 10px; list-style: none; font-size: 14px; color: var(--text-dark); }
  .contacts li { display: flex; align-items: center; gap: 8px; line-height: 1.45; }
  .contacts svg { width: 14px; height: 14px; flex: none; fill: var(--brand-red); }
</style>
</head>
<body>
<main class="stage">

  <section class="card card--back" aria-label="Card back">
    <div class="brand">
      <span class="brand__dot"></span>
      <span class="brand__name">Nomadia</span>
    </div>
    <p class="web">www.nomadia.example</p>
  </section>

  <section class="card card--front" aria-label="Card front">
    <svg class="front__panel" viewBox="0 0 560 320" preserveAspectRatio="none" aria-hidden="true">
      <polygon points="330,0 560,0 560,320 270,320" fill="var(--card-dark)"/>
      <circle cx="432" cy="210" r="104" fill="var(--brand-red)"/>
    </svg>

    <div class="front__content">
      <div class="front__brand">Nomadia</div>
      <div class="person">
        <p class="person__name">Clara Voss</p>
        <p class="person__role">Director</p>
      </div>
      <p class="address">Unit 48 Harbour Lane<br>Westport, 5170, Norland</p>
      <ul class="contacts">
        <li>
          <svg viewBox="0 0 16 16"><path d="M3 2h3l1 4-2 1a9 9 0 0 0 4 4l1-2 4 1v3a2 2 0 0 1-2 2C6 15 1 10 1 4a2 2 0 0 1 2-2z"/></svg>
          210 555 0142
        </li>
        <li>
          <svg viewBox="0 0 16 16"><path d="M4 1h8v14H4zM5.5 3v9h5V3z"/></svg>
          210 555 0187
        </li>
        <li>
          <svg viewBox="0 0 16 16"><path d="M4 1h7v4H4zM1 6h14v7h-3v2H4v-2H1zM5 10v4h6v-4z"/></svg>
          210 555 0187
        </li>
        <li>
          <svg viewBox="0 0 16 16"><path d="M1 3h14v10H1zM2.5 4.5 8 9l5.5-4.5z"/></svg>
          hello@nomadia.example
        </li>
        <li>
          <svg viewBox="0 0 16 16"><path d="M8 1a7 7 0 1 0 0 14A7 7 0 0 0 8 1zm0 1.5c1 1.2 1.6 3 1.7 4.8H6.3C6.4 5.5 7 3.7 8 2.5zM2.6 7.3h2.2c.1-1.6.5-3 1.2-4.2a5.5 5.5 0 0 0-3.4 4.2zm0 1.4A5.5 5.5 0 0 0 6 12.9c-.7-1.2-1.1-2.6-1.2-4.2zm3.7 0h3.4c-.1 1.8-.7 3.6-1.7 4.8-1-1.2-1.6-3-1.7-4.8zm4.9 0c-.1 1.6-.5 3-1.2 4.2a5.5 5.5 0 0 0 3.4-4.2zm2.2-1.4A5.5 5.5 0 0 0 10 3.1c.7 1.2 1.1 2.6 1.2 4.2z"/></svg>
          www.nomadia.example
        </li>
      </ul>
    </div>
  </section>

</main>
</body>
</html>
```